Kelvo.cn needs pages to be re-designed

www.kelvo.cn is our current new site which was launched in April.
We're a financial services website in the crowdfunding space in China to connect borrower's and lender's.

test.kelvo.cn is our test site
u: test
p: fogpine
http://test.kelvo.cn/
http://test.kelvo.cn/user/accounts/new_lender
http://test.kelvo.cn/user/accounts/new_borrower
http://test.kelvo.cn/introductions/protection
http://test.kelvo.cn/introductions
http://test.kelvo.cn/introductions/kelvo_admin
http://test.kelvo.cn/introductions/contact
Some of the pages have pop-ups in the bloc's of the pages. Please click the links, to see more content.

User's currently criticize the website for being:
- Too Western looking
- Too simple, too little content
- Content NOT in the pop-ups are too simple
- Pictures are too big and too much blank space
- Relevant information is not there when needed
- The pictures are too generic

What we would like to do is re-design those pages with the same color scheme and style to be more compelling, efficient, non-intimidating and easy-to-use. Our audience is Ages 25-35 predominantly male investors.
We are looking for more ideas to make the content match the style, while bridging western and chinese design. Our ultimate goal is to increase registrants to the website and highlight our core competitive advantages.

Some competitors websites are:
www.tobumix.com
www.fesca.com
www.zwqvolt.com

Reason: Not enough good designs that follow the prompt. Same style, better information layout!

Reason: Still have not received a design we're satisfied with

Reason: WE DONT WANT A COMPLETE REDESIGN OF PAGES . KEEP THE EXACT SAME COLOR AND STYLE - WE WANT CONTENT RE-DESIGN! THE BLOCS ARE TOO SIMPLE - WE WANT MORE CONTENT INSIDE.

Reason: no new designs

Reason: no new designs

Reason: other non-registered pages need to be re-designed

```html
<!DOCTYPE html>
<html lang="zh-CN">
<head>
<meta charset="utf-8">
<title>Kelvo.cn 首页</title>
<link href="https://fonts.googleapis.com/css2?family=Noto+Sans+SC:wght@400;500;700&display=swap" rel="stylesheet">
<style>
:root{
  --green:#4caf2a;
  --green-dark:#33861a;
  --green-text:#3f9a1e;
  --blue:#1b84d8;
  --blue-bar:#2a97e6;
  --ink:#2d2d2d;
  --muted:#777;
  --line:#e2e2e2;
  --topbar:#2b2b2b;
  --band:#eef2f5;
  --footer:#25272b;
  --orange:#f7a23b;
  --yellow:#f6c531;
  --coral:#e86b6b;
  --purple:#9b7b9e;
}
*{box-sizing:border-box;margin:0;padding:0}
html,body{width:1200px;height:2457px;overflow:hidden}
body{font-family:"Noto Sans SC",sans-serif;color:var(--ink);background:#fff;font-size:13px}
.page{position:relative;width:1200px;height:2457px;overflow:hidden;background:#f6f7f8}
.abs{position:absolute}

/* top bar */
.topbar{left:0;top:0;width:1200px;height:36px;background:var(--topbar)}
.topbar .field{top:8px;height:20px;background:#fff;border:1px solid #999;font-size:10px;color:#999;padding:2px 6px;line-height:14px}
.topbar .go{top:8px;left:772px;width:92px;height:20px;background:var(--green);color:#fff;font-size:11px;text-align:center;line-height:20px;border-radius:2px}
.topbar .hint{top:9px;left:877px;color:#ddd;font-size:11px}
.topbar .lang{top:9px;left:1036px;width:24px;height:17px;background:#555;border-radius:2px}

/* header */
.header{left:0;top:36px;width:1200px;height:90px;background:#fff;border-bottom:1px solid var(--line)}
.brand{left:140px;top:24px;display:flex;align-items:center;gap:10px}
.brand .dot{width:40px;height:40px;border-radius:50%;background:var(--green)}
.brand .name{font-size:26px;font-weight:700;color:var(--green-dark)}
.nav a{position:absolute;top:34px;font-size:19px;color:var(--ink);text-decoration:none;font-weight:500;white-space:nowrap}

/* hero */
.hero{left:0;top:126px;width:1200px;height:324px;background:linear-gradient(90deg,#5a4a43 0%,#8f8a86 18%,#cfd2d5 40%,#e8eaec 70%,#f1f2f3 100%)}
.hero-copy{left:655px;top:190px;width:420px}
.hero-copy h1{font-size:40px;line-height:56px;font-weight:700;color:#1e1e1e;letter-spacing:2px;white-space:nowrap}
.hero-copy p{font-size:15px;line-height:28px;color:#333;margin-top:10px;white-space:nowrap}

/* slogan band */
.band{left:0;top:450px;width:1200px;height:134px;background:var(--band)}
.band .left{left:140px;top:34px;color:var(--green-text);font-size:22px;line-height:38px}
.band .mid{left:508px;top:36px;font-size:21px;color:var(--ink);font-weight:500}
.band .date{left:768px;top:78px;font-size:12px;color:var(--muted)}
.btn{background:linear-gradient(#5fc136,#3a9a1d);color:#fff;border-radius:20px;text-align:center;font-weight:500}
.band .cta{left:932px;top:46px;width:126px;height:40px;line-height:40px;font-size:16px}

/* features */
.features{left:0;top:584px;width:1200px;height:286px;background:#fff}
.feature{top:40px;width:300px;text-align:center}
.feature .ico{width:62px;height:62px;border-radius:50%;background:#eef0f1;border:1px solid #dde;margin:0 auto;display:flex;align-items:center;justify-content:center}
.feature h3{font-size:18px;margin-top:12px;font-weight:700}
.feature p{font-size:11px;line-height:19px;color:#555;margin:10px 18px 0}
.feature .more{font-size:11px;color:var(--green-text);margin-top:8px}
.divider{top:50px;width:1px;height:190px;background:var(--line)}

/* rate bar */
.ratebar{left:140px;top:892px;width:918px;height:46px;text-align:center;font-size:22px;line-height:46px;color:var(--blue);font-weight:700}
.ratebar .k{color:var(--ink)}
.arrow{top:902px;color:#aaa;font-size:26px}

/* loans table */
.loans{left:140px;top:962px;width:918px;height:378px;background:#fff;border:1px solid var(--line)}
.loans .head{left:0;top:0;width:916px;height:44px;background:#eeeeee;font-weight:700;font-size:16px}
.loans .head span,.row span{position:absolute;white-space:nowrap}
.row{left:0;width:916px;height:50px;border-bottom:1px solid #eee;font-size:12px;color:#444}
.row.alt{background:#f5f6f7}
.badge{display:inline-block;width:15px;height:15px;border-radius:50%;color:#fff;font-size:9px;text-align:center;line-height:15px;margin-right:3px;font-style:normal}
.bar{display:inline-block;width:60px;height:6px;background:#ddd;border-radius:3px;vertical-align:middle}
.bar i{display:block;width:5px;height:6px;background:var(--green);border-radius:3px}
.pill{background:var(--blue);color:#fff;font-size:10px;border-radius:10px;padding:1px 10px}

/* stats */
.stat .v{font-size:21px;font-weight:700}
.stat .l{font-size:10px;color:var(--muted);margin-top:4px}

/* popups */
.popup{background:#fff;border:1px solid #ddd;box-shadow:0 2px 10px rgba(0,0,0,.25)}
.form-row{position:absolute;font-size:12px;color:#444;white-space:nowrap}
.form-row .in{position:absolute;height:32px;border:1px solid #ccc;background:#fff}

/* products */
.products-title{left:140px;top:1512px;font-size:21px;font-weight:700;color:var(--green-dark)}
.product{top:1566px;width:229px;height:192px;color:#fff;padding:22px 18px}
.product .t{font-size:12px}
.product .r{font-size:26px;font-weight:700;margin-top:10px}
.product .d{font-size:11px;margin-top:2px}
.product .b{position:absolute;left:18px;top:128px;width:98px;height:34px;line-height:34px;font-size:14px}

/* banks */
.banks-title{left:620px;top:1804px;font-size:21px;font-weight:700}
.bank{height:18px;border-radius:3px}

/* partners */
.partners{left:0;top:2014px;width:1200px;height:96px;background:#e3e3e3}
.partner{top:40px;font-size:15px;font-weight:500;color:#3a3a3a;white-space:nowrap}

/* contact bar */
.contact{left:154px;top:2114px;width:902px;height:58px;background:var(--blue-bar)}
.social{top:13px;width:32px;height:32px;border-radius:50%;background:#fff}
.contact .ask{left:235px;top:12px;width:222px;height:34px;line-height:34px;font-size:13px}
.contact .tel{left:491px;top:6px;color:#fff;font-size:11px}
.contact .tel b{display:block;font-size:22px;letter-spacing:1px}
.contact .side{top:12px;color:#fff;font-size:10px;line-height:17px}

/* footer */
.footer{left:0;top:2172px;width:1200px;height:285px;background:var(--footer)}
.links{left:0;width:1200px;text-align:center;color:#ddd;font-size:11px;word-spacing:24px}
.cert{top:154px;width:84px;height:40px;background:#d6d6d6;border-radius:3px}
.copy{left:0;top:254px;width:1200px;text-align:center;color:#888;font-size:11px}
</style>
</head>
<body>
<div class="page">

  <div class="abs topbar">
    <div class="abs field" style="left:358px;width:195px">搜索借款 · 项目编号</div>
    <div class="abs field" style="left:567px;width:191px">输入您的注册邮箱</div>
    <div class="abs go">免费注册</div>
    <div class="abs hint">已有账号请直接登录</div>
    <div class="abs lang"></div>
  </div>

  <header class="abs header">
    <div class="abs brand"><span class="dot"></span><span class="name">Kelvo.cn</span></div>
    <nav class="nav">
      <a style="left:496px">借款人服务中心</a>
      <a style="left:706px">投资理财与保障计划</a>
      <a style="left:942px">关于我们与帮助</a>
    </nav>
  </header>

  <section class="abs hero" role="img" aria-label="Photo of a smiling businesswoman in front of a team of colleagues in an office"></section>
  <div class="abs hero-copy">
    <h1>连接借贷双方信任<br>稳健增值 轻松理财</h1>
    <p>本息保障计划全程守护 · 资金托管 · 风险备用金<br>专业团队严格审核 · 多重风控 · 透明公开<br>足不出户 网上轻松投资理财收益<br>门槛低、收益高 让财富稳步增长</p>
  </div>

  <section class="abs band">
    <div class="abs left">助 力您的梦想实现<br>投资 助力 创业 为未来</div>
    <div class="abs mid">用借款，自筹致富梦 自 利！</div>
    <div class="abs date">2014-07-17</div>
    <svg class="abs" style="left:850px;top:50px" width="80" height="30" viewBox="0 0 80 30"><path d="M2 24 Q40 30 74 10" fill="none" stroke="#333" stroke-width="1.5"/><path d="M66 8 L76 9 L71 17" fill="none" stroke="#333" stroke-width="1.5"/></svg>
    <div class="abs btn cta">立即申请 ▶</div>
  </section>

  <section class="abs features">
    <div class="abs feature" style="left:131px">
      <div class="ico"><svg width="26" height="24"><rect x="2" y="14" width="5" height="10" fill="#f2a23a"/><rect x="10" y="8" width="5" height="16" fill="#4caf2a"/><rect x="18" y="2" width="5" height="22" fill="#1b84d8"/></svg></div>
      <h3>收益高</h3>
      <p>年化收益率最高可达15%，远超银行<br>理财，收益稳定可预期，投资门槛低<br>百元起投，资金灵活安排</p>
      <div class="more">了解更多 &nbsp; 立即投资</div>
    </div>
    <div class="abs divider" style="left:420px"></div>
    <div class="abs feature" style="left:442px">
      <div class="ico"><svg width="22" height="26"><rect x="2" y="11" width="18" height="14" rx="2" fill="#888"/><path d="M6 11 V7 a5 5 0 0 1 10 0 V11" fill="none" stroke="#888" stroke-width="2.5"/></svg></div>
      <h3>安全</h3>
      <p>本金保障计划，风险备用金专户<br>托管，借款人严格审核，全程电子<br>合同保护，让您安心放心投资</p>
      <div class="more">了解更多 &nbsp; 立即投资</div>
    </div>
    <div class="abs divider" style="left:768px"></div>
    <div class="abs feature" style="left:796px">
      <div class="ico"><svg width="26" height="26"><circle cx="13" cy="13" r="10" fill="none" stroke="#888" stroke-width="2"/><circle cx="13" cy="13" r="4" fill="#888"/></svg></div>
      <h3>快</h3>
      <p>在线申请，快速审核，最快当天<br>放款。流程简单透明，随时查看<br>借款进度，操作方便快捷</p>
      <div class="more">了解更多 &nbsp; 立即投资</div>
    </div>
  </section>

  <div class="abs arrow" style="left:140px">‹</div>
  <div class="abs ratebar">投资 代 <span class="k">50000元 年利率15.0%</span> &nbsp;&nbsp; 借款台 <span class="k">130元 年利率15.0%</span></div>
  <div class="abs arrow" style="left:1044px">›</div>

  <section class="abs loans">
    <div class="abs head">
      <span style="left:24px;top:10px">借款标</span>
      <span style="left:264px;top:10px">信用等级</span>
      <span style="left:362px;top:10px">年利率</span>
      <span style="left:454px;top:10px">借款金额</span>
      <span style="left:596px;top:10px">期限</span>
      <span style="left:688px;top:10px">进度</span>
    </div>
    <div class="abs row" style="top:56px">
      <span style="left:24px;top:18px">个体商户经营周转借款 · 用于扩大店铺</span>
      <span style="left:264px;top:16px"><i class="badge" style="background:var(--green)">A</i><i class="badge" style="background:var(--green)">✓</i></span>
      <span style="left:362px;top:18px">15.0%</span>
      <span style="left:454px;top:18px">50,000 元</span>
      <span style="left:596px;top:18px">12 个月</span>
      <span style="left:688px;top:16px"><i class="bar"><i></i></i> &nbsp;6.69%</span>
      <span style="left:830px;top:16px" class="pill">投标</span>
    </div>
    <div class="abs row alt" style="top:110px">
      <span style="left:24px;top:18px">教育培训机构借款 · 购置教学设备</span>
      <span style="left:264px;top:16px"><i class="badge" style="background:var(--green)">A</i><i class="badge" style="background:var(--green)">✓</i><i class="badge" style="background:var(--blue)">保</i></span>
    </div>
    <div class="abs row" style="top:160px">
      <span style="left:24px;top:18px">网店进货周转 · 旺季备货</span>
      <span style="left:264px;top:16px"><i class="badge" style="background:var(--green)">B</i><i class="badge" style="background:var(--green)">✓</i><i class="badge" style="background:var(--blue)">保</i></span>
      <span style="left:362px;top:18px">14.52%</span>
    </div>
    <div class="abs row alt" style="top:212px">
      <span style="left:24px;top:18px">餐饮门店装修借款 · 翻新店面提升客流</span>
      <span style="left:264px;top:16px"><i class="badge" style="background:var(--green)">A</i><i class="badge" style="background:var(--green)">✓</i></span>
      <span style="left:362px;top:18px">15.0%</span>
    </div>
    <div class="abs row" style="top:262px">
      <span style="left:24px;top:18px">物流车辆购置 · 扩充运输能力</span>
      <span style="left:264px;top:16px"><i class="badge" style="background:var(--green)">A</i><i class="badge" style="background:var(--green)">✓</i></span>
      <span style="left:362px;top:18px">15.0%</span>
    </div>
    <div class="abs row" style="top:314px;border:none">
      <span style="left:24px;top:16px">个人消费 · 装修新房</span>
      <span style="left:264px;top:14px"><i class="badge" style="background:var(--green)">A</i><i class="badge" style="background:var(--green)">✓</i></span>
      <span style="left:362px;top:16px">15.0%</span>
    </div>
  </section>

  <div class="abs stat" style="left:140px;top:1388px"><div class="v">¥ 160407</div><div class="l">平台累计成交金额 · 投资总额</div></div>
  <div class="abs stat" style="left:365px;top:1388px"><div class="v">14.69%</div><div class="l">平均年化收益率 · 投资回报</div></div>

  <aside class="abs popup" style="left:594px;top:1071px;width:466px;height:470px">
    <div class="abs" style="left:18px;top:30px;font-size:18px;color:var(--blue);font-weight:500">快速申请借款</div>
    <div class="form-row" style="left:22px;top:92px;width:420px">借款金额（元）<span class="in" style="left:142px;top:-8px;width:286px"></span></div>
    <div class="form-row" style="left:22px;top:140px;width:420px">真实姓名<span class="in" style="left:142px;top:-8px;width:286px"></span></div>
    <div class="form-row" style="left:22px;top:188px;width:420px">手机号码<span class="in" style="left:142px;top:-8px;width:286px"></span></div>
    <div class="form-row" style="left:22px;top:236px;width:420px">借款期限<span class="in" style="left:142px;top:-8px;width:286px"></span></div>
    <div class="form-row" style="left:22px;top:284px;width:420px">城市<span class="in" style="left:142px;top:-8px;width:286px"></span></div>
    <div class="form-row" style="left:22px;top:332px;width:420px">验证码<span class="in" style="left:142px;top:-8px;width:176px"></span><b style="position:absolute;left:334px;top:-4px;font-size:18px">学舞合算</b></div>
    <div class="form-row" style="left:138px;top:380px;font-size:10px"><span style="display:inline-block;width:11px;height:11px;border:1px solid #999;vertical-align:middle"></span> &nbsp;我已阅读并同意 &nbsp;<span style="color:var(--green-text)">《借款服务协议》</span></div>
    <div class="form-row" style="left:212px;top:436px;font-size:11px">提交后 客服 联系</div>
    <div class="abs btn" style="left:338px;top:424px;width:92px;height:38px;line-height:38px;font-size:15px">提交</div>
  </aside>

  <h2 class="abs products-title">投资理财计划</h2>
  <div class="abs product" style="left:140px;background:var(--orange)"><div class="t">月月盈投资计划</div><div class="r">10.0%</div><div class="d">预期年化，低门槛稳健收益</div><div class="btn b">立即加入</div></div>
  <div class="abs product" style="left:370px;background:var(--yellow)"><div class="t">季季盈投资计划</div><div class="r">11.0%</div><div class="d">预期年化，低门槛稳健收益</div><div class="btn b">立即加入</div></div>
  <div class="abs product" style="left:600px;background:var(--coral)"><div class="t">半年盈投资计划</div><div class="r">12.0%</div><div class="d">预期年化，低门槛稳健收益</div><div class="btn b">立即加入</div></div>
  <div class="abs product" style="left:829px;background:var(--purple)"><div class="t">年年盈投资计划</div><div class="r">13.0%</div><div class="d">预期年化，低门槛稳健收益</div><div class="btn b">立即加入</div></div>

  <div class="abs arrow" style="left:140px;top:1876px">‹</div>
  <h2 class="abs banks-title">与多家银行合作托管</h2>
  <div class="abs bank" style="left:615px;top:1884px;width:60px;background:#e5a6a6"></div>
  <div class="abs bank" style="left:700px;top:1880px;width:70px;background:#e28a8a"></div>
  <div class="abs bank" style="left:810px;top:1880px;width:70px;background:#e07070"></div>
  <div class="abs bank" style="left:610px;top:1912px;width:60px;background:#8fb0d6"></div>
  <div class="abs bank" style="left:700px;top:1912px;width:76px;background:#9cc79c"></div>
  <div class="abs bank" style="left:810px;top:1910px;width:70px;background:#d77575"></div>
  <div class="abs arrow" style="left:1044px;top:1876px">›</div>

  <aside class="abs popup" style="left:160px;top:1737px;width:512px;height:210px">
    <div class="form-row" style="left:24px;top:36px;width:470px">投资金额<span class="in" style="left:112px;top:-8px;width:296px"></span></div>
    <div class="form-row" style="left:24px;top:84px;width:470px">手机号码<span class="in" style="left:112px;top:-8px;width:296px"></span></div>
    <div class="abs btn" style="left:136px;top:120px;width:130px;height:36px;line-height:36px;font-size:14px">立即开始投资</div>
    <div class="form-row" style="left:278px;top:130px;font-size:11px">◎ 怎么投？</div>
    <div class="form-row" style="left:142px;top:178px;font-size:10px"><span style="display:inline-block;width:10px;height:10px;border:1px solid #999;vertical-align:middle"></span> &nbsp;我已阅读并同意 · 投资协议</div>
  </aside>

  <section class="abs partners">
    <span class="abs partner" style="left:140px">■ Aurelo Direct</span>
    <span class="abs partner" style="left:305px">Microfin Alliance</span>
    <span class="abs partner" style="left:485px;font-size:21px;top:34px">CloudNimbus</span>
    <span class="abs partner" style="left:695px">Drelia</span>
    <span class="abs partner" style="left:785px">Corvan Credit</span>
    <span class="abs partner" style="left:910px;font-size:12px;top:42px">Meridon Credit Services</span>
  </section>

  <section class="abs contact">
    <span class="abs social" style="left:20px;border-radius:4px"></span>
    <span class="abs social" style="left:70px"></span>
    <span class="abs social" style="left:120px"></span>
    <span class="abs social" style="left:170px"></span>
    <div class="abs btn ask">在线咨询客服 · 获取专属投资顾问</div>
    <div class="abs tel">全国免费客服热线 · 工作日 9:00-18:00<b>400 - 016 - 7788</b></div>
    <div class="abs side" style="left:720px">投资理财咨询 &nbsp; 借款服务<br>客服邮件 &nbsp; 在线留言</div>
  </section>

  <footer class="abs footer">
    <div class="abs links" style="top:44px">关于我们 新闻 借款服务中心 帮助 理财投资 保障 风险控制 本息保障计划 安全 招贤纳士 联系我们</div>
    <div class="abs links" style="top:75px">借款服务中心与投资理财 投资理财与保障计划 网站地图 投资保障计划说明</div>
    <div class="abs links" style="top:106px">新手指引 常见问题 服务协议 隐私条款 友情链接</div>
    <div class="abs cert" style="left:278px"></div>
    <div class="abs cert" style="left:390px"></div>
    <div class="abs cert" style="left:502px"></div>
    <div class="abs cert" style="left:614px"></div>
    <div class="abs cert" style="left:726px"></div>
    <div class="abs cert" style="left:838px"></div>
    <div class="abs copy">© 2014 Kelvo.cn 版权所有 &nbsp; 网络借贷信息服务平台</div>
  </footer>

</div>
</body>
</html>
```